KPT Building And Maintenance

Need a very professional looking double sided Buisiness card with all my details phone number, name, email, license number.

Target Market(s)

construction industry

Industry/Entity Type

building

Contact Information for Business Card

Name Dale Whitcombe. Email Address Info@KPTBuilding.example.au mobile number 0452918730 licence number 871406D. web site

```html
<!DOCTYPE html>
<html lang="en">
<head>
<meta charset="utf-8">
<title>KPT Building And Maintenance – Business Card</title>
<link rel="stylesheet" href="https://fonts.googleapis.com/css2?family=Roboto+Condensed:wght@400;500;700&family=Source+Sans+3:wght@400&display=swap">
<style>
  :root {
    --backdrop: #9a9b9b;
    --card-white: #ffffff;
    --brand-blue: #2b9fdc;
    --wave-blue: #46a4dc;
    --wave-grey: #7d7e80;
    --ink-grey: #555759;
    --ink-dark: #3a3c3e;
  }
  * { box-sizing: border-box; margin: 0; padding: 0; }
  html, body {
    width: 1200px; height: 1200px; overflow: hidden;
    background: var(--backdrop);
  }
  .canvas { position: relative; width: 1200px; height: 1200px; }

  .card {
    position: absolute; left: 222px; width: 755px; height: 463px; overflow: hidden;
  }
  .card-front {
    top: 105px; background: var(--card-white);
    border-radius: 0 36px 0 36px;
  }
  .card-back {
    top: 630px; background: var(--brand-blue);
    border-radius: 36px 0 36px 0;
  }

  .front-brand {
    position: absolute; left: 46px; top: 200px;
    display: flex; align-items: center; gap: 12px;
    font-family: "Roboto Condensed", sans-serif; font-weight: 700;
    color: var(--brand-blue); text-transform: uppercase;
    font-size: 25px; line-height: 1.05; letter-spacing: 0.5px;
  }
  .front-brand .brand-square {
    width: 46px; height: 46px; background: var(--brand-blue); flex: none;
  }

  .divider {
    position: absolute; left: 412px; top: 119px; width: 2px; height: 227px;
    background: var(--brand-blue);
  }

  .contact-block { position: absolute; left: 444px; top: 112px; width: 280px; }
  .person-name {
    font-family: "Roboto Condensed", sans-serif; font-weight: 700;
    font-size: 36px; color: var(--brand-blue); line-height: 1.1;
    white-space: nowrap;
  }
  .person-role {
    font-family: "Roboto Condensed", sans-serif; font-weight: 400;
    font-size: 23px; color: var(--ink-grey); line-height: 1.1;
  }
  .licence {
    margin-top: 16px;
    font-family: "Source Sans 3", sans-serif; font-size: 21px; color: var(--ink-dark);
    white-space: nowrap;
  }
  .licence .label { color: var(--brand-blue); }
  .contact-list { list-style: none; margin-top: 22px; }
  .contact-list li {
    display: flex; align-items: center; gap: 9px; height: 33px;
    font-family: "Source Sans 3", sans-serif; font-size: 19px; color: var(--ink-dark);
    white-space: nowrap;
  }
  .contact-list svg { width: 20px; height: 20px; flex: none; }

  .front-wave { position: absolute; left: 0; top: 0; width: 755px; height: 463px; }

  .back-map {
    position: absolute; left: 10px; top: 50px; width: 735px; height: 400px;
    background: radial-gradient(ellipse at 50% 45%, rgba(255,255,255,0.10), rgba(255,255,255,0.03) 60%, rgba(255,255,255,0) 75%);
  }
  .back-brand {
    position: absolute; left: 0; right: 0; top: 220px; text-align: center;
    font-family: "Roboto Condensed", sans-serif; font-weight: 700;
    color: var(--card-white); text-transform: uppercase;
    font-size: 72px; line-height: 1; letter-spacing: 2px;
  }
</style>
</head>
<body>
<main class="canvas">

  <section class="card card-front" aria-label="Business card front">
    <svg class="front-wave" viewBox="0 0 755 463" aria-hidden="true">
      <path d="M0,426 C150,392 310,392 500,428 C620,450 700,452 755,438 L755,463 L0,463Z" fill="var(--wave-grey)"/>
      <path d="M0,440 C170,404 330,408 520,438 C640,456 710,452 755,434 L755,463 L0,463Z" fill="var(--card-white)"/>
      <path d="M6,450 C180,414 340,418 530,446 C650,462 715,456 755,444 L755,463 L0,463Z" fill="var(--wave-blue)"/>
    </svg>

    <div class="front-brand">
      <span class="brand-square"></span>
      <span>KPT Building and<br>Maintenance</span>
    </div>

    <div class="divider"></div>

    <div class="contact-block">
      <h1 class="person-name">Dale Whitcombe</h1>
      <p class="person-role">Owner</p>
      <p class="licence"><span class="label">licence number</span> 871406D</p>
      <ul class="contact-list">
        <li>
          <svg viewBox="0 0 24 24" aria-hidden="true"><path fill="var(--brand-blue)" d="M6.6 10.8a15.1 15.1 0 0 0 6.6 6.6l2.2-2.2a1 1 0 0 1 1-.25 11.4 11.4 0 0 0 3.6.57 1 1 0 0 1 1 1V20a1 1 0 0 1-1 1A17 17 0 0 1 3 4a1 1 0 0 1 1-1h3.5a1 1 0 0 1 1 1c0 1.25.2 2.45.57 3.57a1 1 0 0 1-.25 1z"/></svg>
          0452918730
        </li>
        <li>
          <svg viewBox="0 0 24 24" aria-hidden="true"><rect x="2" y="5" width="18" height="13" rx="1.5" fill="var(--brand-blue)"/><path d="M3 6.5l8 6 8-6" fill="none" stroke="#fff" stroke-width="1.5"/><circle cx="19" cy="18" r="4.5" fill="var(--brand-blue)" stroke="#fff" stroke-width="1.2"/><path d="M17 18l1.5 1.5 2.5-2.8" fill="none" stroke="#fff" stroke-width="1.3"/></svg>
          Info@KPTBuilding.example.au
        </li>
        <li>
          <svg viewBox="0 0 24 24" aria-hidden="true"><g fill="none" stroke="var(--brand-blue)" stroke-width="1.6"><circle cx="12" cy="12" r="9.5"/><ellipse cx="12" cy="12" rx="4.2" ry="9.5"/><path d="M2.5 12h19M4 7h16M4 17h16"/></g></svg>
          www.KPTBuilding.example.au
        </li>
      </ul>
    </div>
  </section>

  <section class="card card-back" aria-label="Business card back">
    <div class="back-map" role="img" aria-label="Faint world map in light blue behind the company name"></div>
    <p class="back-brand">KPT Building</p>
  </section>

</main>
</body>
</html>
```